Calm and Compass Health Flyer (new business startup)

One page...clear enough to be read if faxed. This mental health clinic treats depression/anxiety in kids and adults. It also treats opiate and alcohol addiction. It's in downtown Elmira, NY and the owner of the clinic is from Elmira NY, where it's located. This clinic does not take health insurance, so it charges a low rate of $75 a visit once they pay the $125 starting fee.

Target Market(s)

doctors offices, new patients

Industry/Entity Type

Doctor

Requirements
Must have
• see microsoft word document. pdf is printed on the company letterhead.
Nice to have
• a simplified map would be nice. if you can include the building it would be a plus. The same two fonts were used in the business cards and letter head (kennedy small caps boo*) and Refrigerator Delux.

```html
<!DOCTYPE html>
<html lang="en">
<head>
<meta charset="utf-8">
<title>Calm &amp; Compass Health – Flyer</title>
<link rel="stylesheet" href="https://fonts.googleapis.com/css2?family=Marcellus&family=Montserrat:wght@600;700&family=Open+Sans:ital,wght@0,400;0,600;1,400&display=swap">
<style>
  :root {
    --cyan: #2fc4ec;
    --blue: #1ea3dc;
    --deep-blue: #1b8fd0;
    --orange: #f26a2e;
    --grey: #8a8a8a;
    --white: #ffffff;
    --sky-top: #4d8fd6;
    --brick: #9a5a3e;
    --street: #b9b4ac;
  }
  html, body {
    margin: 0;
    padding: 0;
    overflow: hidden;
    background: var(--white);
  }
  .flyer {
    position: relative;
    width: 800px;
    height: 1200px;
    overflow: hidden;
    background: var(--white);
    font-family: "Open Sans", Arial, sans-serif;
  }
  .building-photo {
    position: absolute;
    left: 0; top: 0;
    width: 800px; height: 560px;
    background: linear-gradient(180deg, var(--sky-top) 0%, #8fbbe6 18%, var(--brick) 32%, #8a5038 62%, var(--street) 78%, #c9c4bb 100%);
  }
  .swooshes {
    position: absolute;
    left: 0; top: 0;
    width: 800px; height: 600px;
  }
  .brand {
    position: absolute;
    left: 40px; top: 590px;
    display: flex;
    align-items: center;
    gap: 14px;
  }
  .brand-dot {
    width: 62px; height: 62px;
    border-radius: 50%;
    background: var(--orange);
  }
  .brand-name {
    font-family: "Montserrat", Arial, sans-serif;
    font-weight: 700;
    font-size: 26px;
    color: var(--orange);
    letter-spacing: -0.3px;
  }
  .practice-name {
    position: absolute;
    left: 0; top: 658px;
    width: 800px;
    text-align: center;
    font-family: "Marcellus", Georgia, serif;
    font-size: 50px;
    color: var(--cyan);
    letter-spacing: 0.5px;
    margin: 0;
    font-weight: 400;
  }
  .contact-line {
    position: absolute;
    left: 0; top: 716px;
    width: 800px;
    text-align: center;
    font-family: "Open Sans", Arial, sans-serif;
    font-size: 14px;
    font-weight: 600;
    color: var(--blue);
    transform: scaleX(0.9);
  }
  .hours-bar {
    position: absolute;
    left: 110px; top: 767px;
    width: 568px; height: 29px;
    background: var(--cyan);
    color: var(--white);
    font-size: 21px;
    font-weight: 600;
    line-height: 29px;
    padding-left: 26px;
    box-sizing: border-box;
  }
  .price-list {
    position: absolute;
    left: 52px; top: 818px;
    width: 672px;
    margin: 0; padding: 0;
    list-style: none;
  }
  .price-item {
    display: flex;
    align-items: baseline;
    height: 39px;
  }
  .price-label {
    font-family: "Montserrat", Arial, sans-serif;
    font-weight: 600;
    font-size: 20px;
    color: var(--grey);
    white-space: nowrap;
  }
  .price-dots {
    flex: 1;
    margin: 0 4px 0 18px;
    border-bottom: 4px dotted var(--blue);
    transform: translateY(-4px);
  }
  .price-amount {
    font-family: "Montserrat", Arial, sans-serif;
    font-weight: 700;
    font-size: 28px;
    color: var(--blue);
  }
  .ages {
    position: absolute;
    left: 0; top: 913px;
    width: 800px;
    text-align: center;
    font-family: "Montserrat", Arial, sans-serif;
    font-weight: 700;
    font-size: 27px;
    color: var(--blue);
    margin: 0;
  }
  .conditions {
    position: absolute;
    left: 100px; top: 978px;
    width: 600px;
    text-align: center;
    font-size: 20px;
    line-height: 30px;
    color: var(--grey);
    margin: 0;
  }
  .conditions strong {
    font-family: "Montserrat", Arial, sans-serif;
    font-weight: 700;
  }
  .motto {
    position: absolute;
    left: 0; top: 1068px;
    width: 800px;
    text-align: center;
    font-style: italic;
    font-size: 21px;
    color: var(--blue);
    margin: 0;
  }
  .insurance-note {
    position: absolute;
    left: 40px; top: 1112px;
    width: 730px;
    text-align: center;
    font-style: italic;
    font-size: 14px;
    line-height: 20px;
    color: var(--orange);
    margin: 0;
  }
  .footer-band {
    position: absolute;
    left: 0; top: 1178px;
    width: 800px; height: 22px;
  }
</style>
</head>
<body>
<main class="flyer">
  <div class="building-photo" role="img" aria-label="Photo of the clinic's three-storey brick office building on a downtown street corner under a blue sky"></div>

  <svg class="swooshes" viewBox="0 0 800 600" aria-hidden="true">
    <path d="M0,300 C120,400 300,470 520,500 C640,515 730,470 800,420 L800,600 L0,600 Z" fill="var(--white)"/>
    <path d="M0,300 C120,400 300,470 520,500 C640,515 730,470 800,420 L800,440 C720,500 630,530 520,528 C300,520 120,460 0,380 Z" fill="var(--orange)"/>
    <path d="M0,440 C150,520 350,550 620,520 C430,565 200,560 0,500 Z" fill="var(--blue)"/>
    <path d="M470,455 C600,440 720,400 800,350 L800,372 C720,420 600,455 470,455 Z" fill="var(--blue)"/>
  </svg>

  <div class="brand">
    <span class="brand-dot"></span>
    <span class="brand-name">CALM &amp; COMPASS HEALTH</span>
  </div>

  <h1 class="practice-name">DANIEL REYES, RPA, PLLC</h1>
  <div class="contact-line">(607) 555-0148 &nbsp;•&nbsp; Psychiatric Physician Assistant (PA-C, PSY-CAQ) &nbsp;•&nbsp; danielreyes@calmcompass.net</div>

  <div class="hours-bar">Hours:&nbsp; Monday and Saturdays 9-4pm</div>

  <ul class="price-list">
    <li class="price-item"><span class="price-label">PSYCHIATRIC EVALUATION (45MIN)</span><span class="price-dots"></span><span class="price-amount">$125</span></li>
    <li class="price-item"><span class="price-label">PSYCHIATRIC OFFICE VISIT (15MIN)</span><span class="price-dots"></span><span class="price-amount">$75</span></li>
  </ul>

  <h2 class="ages">AGES:&nbsp; 6 YEARS OLD AND UP</h2>

  <p class="conditions"><strong>CONDITIONS TREATED:</strong>&nbsp; Depression, Anxiety, PTSD, ADHD, Addiction, Bipolar, Childhood Mood Disorders</p>

  <p class="motto">“We work for you, not the insurance companies”</p>

  <p class="insurance-note">*Although we do not partner with any Health Insurance Companies at this time, a bill will be provided to you at the time of service for you to submit to your insurance company.</p>

  <svg class="footer-band" viewBox="0 0 800 22" aria-hidden="true">
    <path d="M0,6 L440,6 L420,22 L0,22 Z" fill="var(--blue)"/>
    <path d="M440,6 L800,0 L800,22 L420,22 Z" fill="var(--orange)"/>
  </svg>
</main>
</body>
</html>
```